Corvane Optics PowerPoint Template

Corvane Optics needs a nice new corporate PowerPoint template, to be used for all types of presentations: sales, business development, finance, board/exec, etc.

I'd like to get a clean layout that reflects the brand (www.corvaneoptics.example), has a bright, interesting title slide, and then minimal graphics on the content slides. Ideally the content slides would have a header, "co" circle part of the Corvane Optics logo (either above or below), copyright/confidential footer, and page #.

About us: we have developed a revolutionary new array camera for mobile devices, providing depth at every pixel. Focus on any subject, change focus (even on multiple subjects) after you take the photo, capture linear measurements, scale and segment your images, change backgrounds, and apply filters, all from any device.
It's not just about megapixels anymore.
See www.corvaneoptics.example for info.

Target Market(s)

The audience for 90% of our presentations is highly educated executives at technology companies.

Industry/Entity Type

Camera

Requirements
Nice to have
• It would be great to show an image in a phone UI on the title slide, similar to the approach on our website.
Helpful to have tagline on title slide: "A smart camera for your smartphone." It may also fit on the content slides - feel free to try.
I attached a product photo, but using it is completely optional.
I'd like the "co" circle on the content slides, but the whole logo on the title slides.
Thanks!

```html
<!DOCTYPE html>
<html lang="en">
<head>
<meta charset="utf-8">
<title>Corvane Optics – Executive Team</title>
<link rel="stylesheet" href="https://fonts.googleapis.com/css2?family=Open+Sans:ital,wght@0,300;0,400;0,600;1,400&display=swap">
<style>
  :root {
    --brand: #15698f;
    --brand-deep: #0f5475;
    --ink: #3a3a3a;
    --muted: #8a8a8a;
    --paper: #ffffff;
    --dim: rgba(0, 0, 0, 0.5);
    --rule: #b9b9b9;
    --alert: #e41e1e;
    --photo-a: #9aa3a6;
    --photo-b: #5d6a66;
  }
  * { margin: 0; padding: 0; box-sizing: border-box; }
  html, body { width: 1200px; height: 899px; overflow: hidden; }
  body { font-family: "Open Sans", Arial, sans-serif; background: var(--paper); position: relative; color: var(--ink); }
  .slide { position: absolute; inset: 0; background: var(--paper); }
  .title-bar { position: absolute; left: 0; top: 45px; width: 1200px; height: 45px; background: var(--brand); }
  .title-bar .edge { position: absolute; left: 0; top: 0; width: 50px; height: 45px; background: var(--brand-deep); }
  .brand-name { position: absolute; left: 78px; top: 51px; color: var(--paper); font-weight: 300; font-size: 27px; letter-spacing: 0.5px; }
  .section-name { position: absolute; left: 150px; top: 51px; color: var(--paper); font-weight: 300; font-size: 27px; letter-spacing: 0.5px; }
  .page-label { position: absolute; right: 72px; top: 51px; color: var(--paper); font-weight: 300; font-size: 26px; }
  .page-label small { font-size: 15px; opacity: 0.7; margin-right: 8px; }
  .heading { position: absolute; left: 73px; top: 168px; display: flex; align-items: center; gap: 24px; font-weight: 300; font-size: 25px; }
  .heading .dot { width: 26px; height: 26px; border-radius: 50%; background: var(--brand); }
  .team-photo { position: absolute; left: 72px; top: 249px; width: 654px; height: 310px; background: linear-gradient(160deg, var(--photo-a), var(--photo-b)); }
  .team-list { position: absolute; left: 773px; top: 244px; list-style: none; }
  .team-list li { height: 68px; }
  .team-list .name { font-size: 17px; color: var(--ink); display: block; }
  .team-list .role { font-size: 12px; color: var(--muted); display: block; }
  .mini-nav { position: absolute; left: 592px; top: 768px; display: flex; font-size: 14px; color: var(--muted); }
  .mini-nav span { padding: 0 14px; border-left: 1px solid var(--rule); }
  .mini-nav span:first-child { border-left: 0; }
  .mini-nav .current { color: var(--brand); }
  .footer-band { position: absolute; left: 0; top: 807px; width: 1200px; height: 49px; }
  .footer-band .edge { position: absolute; left: 0; top: 0; width: 60px; height: 49px; background: var(--brand); }
  .footer-band .band { position: absolute; left: 387px; top: 0; right: 0; height: 49px; background: var(--brand); }
  .legal { position: absolute; left: 76px; top: 812px; font-size: 12px; line-height: 22px; color: var(--ink); }
  .tagline { position: absolute; right: 77px; top: 821px; color: var(--paper); font-style: italic; font-size: 13px; }
  .dim { position: absolute; inset: 0; background: var(--dim); }
  .nav-zoom { position: absolute; left: 164px; top: 569px; width: 1004px; height: 166px; background: linear-gradient(180deg, #f6f6f6, #e2e2e2); box-shadow: 0 4px 14px rgba(0,0,0,0.35); }
  .nav-zoom .band { position: absolute; left: 0; bottom: 0; width: 100%; height: 23px; background: var(--brand); }
  .nav-zoom .nav { position: absolute; top: 75px; left: 0; width: 100%; height: 38px; display: flex; align-items: center; font-size: 22px; color: #8f8f8f; }
  .nav-zoom .nav span { position: absolute; transform: translateX(-50%); white-space: nowrap; }
  .nav-zoom .nav .current { color: var(--brand); }
  .nav-zoom .sep { position: absolute; top: 74px; width: 1px; height: 40px; background: #b0b0b0; }
  .callout { position: absolute; left: 0; top: 0; }
</style>
</head>
<body>
  <div class="slide">
    <div class="title-bar"><div class="edge"></div></div>
    <div class="brand-name">co</div>
    <div class="section-name">ABOUT</div>
    <div class="page-label"><small>page</small>EXECUTIVE TEAM</div>

    <div class="heading"><span class="dot"></span>EXECUTIVE TEAM</div>

    <div class="team-photo" role="img" aria-label="Group photo of the executive team standing outside a station building"></div>

    <ul class="team-list">
      <li><span class="name">Martin Halloway</span><span class="role">President &amp; CEO</span></li>
      <li><span class="name">Dev Raghunathan</span><span class="role">Co-Founder &amp; CTO</span></li>
      <li><span class="name">Owen Brackley</span><span class="role">VP Business Development &amp; Marketing</span></li>
      <li><span class="name">Anil R. Mehta</span><span class="role">VP Engineering</span></li>
      <li><span class="name">Colin Rourke</span><span class="role">VP Licensing</span></li>
    </ul>

    <nav class="mini-nav">
      <span>Contact</span><span class="current">Executive Team</span><span>Board of Directors</span><span>About</span><span>Next Page</span>
    </nav>

    <div class="footer-band"><div class="edge"></div><div class="band"></div></div>
    <div class="legal">www.corvaneoptics.example<br>© Corvane Optics 2013. All rights reserved.</div>
    <div class="tagline">A smart camera for your smartphone</div>
  </div>

  <div class="dim"></div>

  <div class="nav-zoom">
    <div class="nav">
      <span style="left:101px">Contact</span>
      <span class="current" style="left:295px">Executive Team</span>
      <span style="left:530px">Board of Directors</span>
      <span style="left:713px">About</span>
      <span style="left:857px">Next Page</span>
    </div>
    <div class="sep" style="left:171px"></div>
    <div class="sep" style="left:402px"></div>
    <div class="sep" style="left:641px"></div>
    <div class="sep" style="left:775px"></div>
    <div class="band"></div>
  </div>

  <svg class="callout" width="1200" height="899" viewBox="0 0 1200 899" aria-hidden="true">
    <circle cx="959" cy="640" r="158" fill="none" stroke="var(--alert)" stroke-width="4"/>
  </svg>
</body>
</html>
```